Home Inspection Report Cover Page- House report

We complete home inspections. This is the very first cover page of our report. We are looking to redesign the front cover page for our inspection reports. The image of the home will change as the property changes. I am providing some initial thoughts for designs. But we are willing to see new and creative designs. We are the predominant company in our industry.

Here is another link to see the first page that we currently have
https://norvaleinspections.com/wp-content/uploads/2019/11/NoPoolNewHomeSample.pdf

People print these reports out so the ink level may be a consideration.

We are looking for a modern design that presents us as an authority.

8.5 x 11

Target Market(s)

Home Buyers and Real Estate Agent

Industry/Entity Type

Home Inspection

Requirements
Must have
• Brand Consistency- Our colors can be found at norvaleinspections.com or in the uploaded Trifold named NV_Trifold

Place for a photograph of the front of a home to be
Nice to have
• Color Gradients

```html
<!DOCTYPE html>
<html lang="en">
<head>
<meta charset="utf-8">
<title>Norvale Group – Inspection Report Cover</title>
<link rel="stylesheet" href="https://fonts.googleapis.com/css2?family=Lato:ital,wght@0,400;0,700;0,900;1,400&family=Russo+One&display=swap">
<style>
  :root{
    --navy:#0c4775;
    --blue:#1f6fb5;
    --blue-dark:#134f86;
    --grey:#9a9c9f;
    --white:#ffffff;
    --stage:#e9eaec;
    --sky-top:#7f8fb4;
    --sky-mid:#c9c2d6;
    --lawn:#6a7a58;
  }
  *{box-sizing:border-box;margin:0;padding:0}
  html,body{width:1200px;height:1200px;overflow:hidden;background:var(--stage)}
  body{font-family:"Lato",sans-serif;position:relative}
  .cover{
    position:absolute;left:175px;top:50px;width:734px;height:950px;
    transform:scale(1.158);transform-origin:0 0;
    background:var(--white);overflow:hidden;
    box-shadow:0 6px 22px rgba(0,0,0,.25);
  }
  .top-band{position:absolute;left:0;top:0;width:734px;height:140px;background:var(--navy)}
  .phone-box{position:absolute;left:488px;top:45px;width:246px;height:60px;background:var(--blue)}
  .phone-icon{position:absolute;left:595px;top:24px;width:36px;height:36px}
  .phone-number{position:absolute;left:488px;top:64px;width:246px;text-align:center;color:var(--white);font-size:28px;font-weight:700;letter-spacing:.5px}
  .order-id{position:absolute;left:488px;top:112px;width:246px;text-align:center;color:var(--white);font-size:16px;letter-spacing:.4px}
  .house-photo{
    position:absolute;left:0;top:138px;width:734px;height:512px;
    background:linear-gradient(180deg,var(--sky-top) 0%,var(--sky-mid) 45%,#8d8f9c 62%,#5f6370 78%,var(--lawn) 100%);
  }
  .brand-panel{
    position:absolute;left:-4px;top:10px;width:500px;height:208px;
    background:var(--white);border:3px solid var(--blue);border-left:none;
    border-radius:0 90px 90px 0;
  }
  .brand-mark{position:absolute;left:196px;top:22px;width:72px;height:72px;border:5px solid var(--blue);border-radius:50%}
  .brand-name{position:absolute;left:0;top:100px;width:466px;text-align:center;font-weight:900;font-size:36px;color:var(--blue);letter-spacing:2px}
  .brand-sub{position:absolute;left:0;top:141px;width:466px;text-align:center;font-weight:700;font-size:14px;color:var(--grey);letter-spacing:.6px}
  .brand-tagline{position:absolute;left:0;top:162px;width:466px;text-align:center;font-style:italic;font-size:10px;color:var(--blue)}
  .services{position:absolute;left:0;top:180px;width:466px;text-align:center;font-weight:700;font-size:16px;color:var(--blue)}
  .location{position:absolute;left:66px;top:632px;width:609px;height:29px}
  .location-text{position:absolute;left:96px;top:638px;color:var(--white);font-size:15px}
  .location-text b{font-weight:900}
  .title{position:absolute;left:0;top:670px;width:734px;text-align:center;font-family:"Russo One",sans-serif;font-size:49px;letter-spacing:-1px;color:var(--blue)}
  .title span{color:var(--grey)}
  .prepared{position:absolute;left:0;top:725px;width:734px;text-align:center;font-size:15px;line-height:20px;color:var(--blue);font-weight:700}
  .prepared .label{font-weight:400}
  .details-band{position:absolute;left:0;top:780px;width:734px;height:170px;background:var(--navy)}
  .details{position:absolute;color:var(--white);font-size:14px;line-height:17px;list-style:none}
  .details li::before{content:"•";color:#6fa8dc;margin-right:6px;font-size:10px}
  .details b{font-weight:700}
  .details-left{left:32px;top:795px}
  .details-right{left:398px;top:792px}
  .badge-panel{
    position:absolute;left:305px;top:840px;width:440px;height:98px;background:var(--white);
    border:3px solid var(--blue);border-right:none;border-radius:60px 0 0 60px;
  }
  .badges{position:absolute;left:385px;top:846px}
  .site-bar{position:absolute;left:0;top:892px;width:318px;height:58px;background:var(--blue);border-top:3px solid var(--white)}
  .site-text{position:absolute;left:58px;top:906px;color:var(--white);font-size:24px}
  .globe{position:absolute;left:24px;top:909px;width:26px;height:26px}
</style>
</head>
<body>
<main class="cover">
  <div class="top-band"></div>
  <div class="phone-box"></div>
  <svg class="phone-icon" viewBox="0 0 36 36" aria-hidden="true">
    <circle cx="18" cy="18" r="16" fill="var(--navy)" stroke="#fff" stroke-width="2"/>
    <path d="M12 11c1-1 2-1 3 0l2 3c.5 1 0 2-1 2.5 1 2 2.5 3.5 4.5 4.5.5-1 1.5-1.5 2.5-1l3 2c1 1 1 2 0 3-2 2-5 1-8-1.5S10 16 12 11z" fill="#fff"/>
  </svg>
  <div class="phone-number">800-555-0142</div>
  <div class="order-id">ORDER ID: 18XXXX</div>

  <div class="house-photo" role="img" aria-label="Photograph of the front of the inspected home at dusk"></div>

  <div class="brand-panel"></div>
  <div class="brand-mark" aria-hidden="true"></div>
  <div class="brand-name">NORVALE GROUP</div>
  <div class="brand-sub">INSPECTION PROFESSIONALS</div>
  <div class="brand-tagline">Inspecting to a Higher Standard Since 1984</div>
  <div class="services">HOME • MOLD • TERMITE • SEWER • COMMERCIAL</div>

  <svg class="location" viewBox="0 0 609 29" aria-hidden="true">
    <polygon points="0,29 12,0 24,0 24,29" fill="var(--blue-dark)"/>
    <polygon points="609,29 597,0 585,0 585,29" fill="var(--blue-dark)"/>
    <rect x="12" y="0" width="585" height="29" fill="var(--blue)"/>
    <path d="M30 6a6 6 0 0 1 6 6c0 4-6 11-6 11s-6-7-6-11a6 6 0 0 1 6-6z" fill="#fff"/>
    <circle cx="30" cy="12" r="2.2" fill="var(--blue)"/>
  </svg>
  <div class="location-text"><b>PROPERTY LOCATION:</b> 1234 Property Address, Any City, CA 92028</div>

  <h1 class="title">INSPECTION<span>REPORT</span></h1>
  <div class="prepared">
    <div><span class="label">PEPARED FOR:</span> CLIENT NAME</div>
    <div><span class="label">REAL ESTATE AGENT:</span> AGENT NAME</div>
  </div>

  <div class="details-band"></div>
  <ul class="details details-left">
    <li><b>Date of Inspection:</b> DD/MM/YYYY</li>
    <li><b>Time:</b> 00:00 PM</li>
    <li><b>Weather:</b> Sunny</li>
  </ul>
  <ul class="details details-right">
    <li><b>Inspector:</b> Sample Report</li>
    <li><b>Email:</b> customerservice@norvaleinspections.com</li>
  </ul>

  <div class="badge-panel"></div>
  <svg class="badges" width="340" height="90" viewBox="0 0 340 90" aria-label="Certification badges">
    <circle cx="92" cy="20" r="18" fill="#e8a13a"/>
    <circle cx="142" cy="20" r="18" fill="#b89b4a"/>
    <circle cx="192" cy="20" r="18" fill="#8fb86a"/>
    <circle cx="14" cy="60" r="18" fill="#c0323a"/>
    <rect x="44" y="44" width="42" height="32" fill="#c9a86a"/>
    <rect x="106" y="44" width="34" height="34" rx="4" fill="#8a8f7a"/>
    <circle cx="172" cy="60" r="18" fill="#4f8f46"/>
    <circle cx="220" cy="60" r="18" fill="#a09a70"/>
    <circle cx="264" cy="58" r="14" fill="none" stroke="#6a5ac8" stroke-width="5"/>
  </svg>

  <div class="site-bar"></div>
  <svg class="globe" viewBox="0 0 26 26" aria-hidden="true" fill="none" stroke="#fff" stroke-width="2">
    <circle cx="13" cy="13" r="11"/>
    <ellipse cx="13" cy="13" rx="5" ry="11"/>
    <line x1="2" y1="13" x2="24" y2="13"/>
  </svg>
  <div class="site-text">norvaleinspections.com</div>
</main>
</body>
</html>
```